Film and TV production company

I have the logo already designed by mark quarry. I just need the text and the logo attached to the business card. Maybe a small design on the back of the card or text.

Industry/Entity Type

film tv arts

Contact Information for Business Card

Dale Morrow Cinematographer-Director

Colors
F0912C
F2A743
F7CA91
FBE8D2
FDF5EE
EE7325
F08F49
F5BC92
FAE3D3
FDF4ED

Requirements
Must have
• www.copperlanepix.com.au my email address mail@copperlanepix.com.au my mobile number 0491570158
Nice to have
• Some kind of small art work on the back that ties in with the logo design attached
Should not have
• Must clean and simple

```html
<!DOCTYPE html>
<html lang="en">
<head>
<meta charset="utf-8">
<title>Copper Lane Pictures – Business Card</title>
<link rel="stylesheet" href="https://fonts.googleapis.com/css2?family=Montserrat:wght@400;500;700&display=swap">
<style>
  :root {
    --canvas: #3a302c;
    --card: #ffffff;
    --ink: #1d1d1d;
    --ink-soft: #333333;
    --accent: #e57d17;
    --accent-deep: #d9701a;
  }
  * { margin: 0; padding: 0; box-sizing: border-box; }
  html, body {
    width: 1200px;
    height: 786px;
    overflow: hidden;
    background: var(--canvas);
    font-family: "Montserrat", sans-serif;
  }
  .stage {
    width: 1200px;
    height: 786px;
    display: flex;
    align-items: center;
    justify-content: center;
    gap: 48px;
  }
  .card {
    width: 520px;
    height: 297px;
    background: var(--card);
    box-shadow: 0 10px 30px rgba(0,0,0,0.45);
    position: relative;
    flex: none;
  }
  /* Front */
  .card-front {
    display: flex;
    align-items: center;
  }
  .brand {
    width: 270px;
    display: flex;
    flex-direction: column;
    align-items: center;
    gap: 14px;
  }
  .brand-dot {
    width: 74px;
    height: 74px;
    border-radius: 50%;
    background: var(--accent);
  }
  .brand-name {
    font-weight: 500;
    font-size: 14px;
    letter-spacing: 2.5px;
    color: var(--ink);
    text-transform: uppercase;
    white-space: nowrap;
  }
  .divider {
    width: 1px;
    height: 96px;
    background: var(--accent);
    flex: none;
  }
  .contact {
    padding-left: 34px;
  }
  .person-name {
    font-weight: 700;
    font-size: 21px;
    color: var(--accent);
    line-height: 1.05;
  }
  .person-role {
    font-size: 10.5px;
    color: var(--ink-soft);
    margin-top: 2px;
  }
  .dash {
    width: 12px;
    height: 1.5px;
    background: var(--accent);
    margin: 12px 0 8px;
  }
  .contact-list { list-style: none; }
  .contact-list li {
    display: flex;
    align-items: center;
    gap: 9px;
    font-size: 11px;
    color: var(--ink-soft);
    line-height: 1.55;
    white-space: nowrap;
  }
  .contact-list svg { width: 10px; height: 10px; flex: none; }
  /* Back */
  .card-back {
    background: linear-gradient(180deg, var(--accent) 0%, var(--accent-deep) 100%);
  }
</style>
</head>
<body>
<main class="stage">
  <section class="card card-front" aria-label="Card front">
    <div class="brand">
      <span class="brand-dot"></span>
      <span class="brand-name">Copper Lane Pictures</span>
    </div>
    <span class="divider"></span>
    <div class="contact">
      <h1 class="person-name">Dale Morrow</h1>
      <p class="person-role">Cinematographer-Director</p>
      <div class="dash"></div>
      <ul class="contact-list">
        <li>
          <svg viewBox="0 0 10 10"><path d="M1 3.5 Q5 0.5 9 3.5 L8 5 L6.5 4.2 L6.5 3.4 Q5 2.9 3.5 3.4 L3.5 4.2 L2 5 Z M2.5 6 H7.5 L8 9 H2 Z" fill="var(--accent)"/></svg>
          0491570158
        </li>
        <li>
          <svg viewBox="0 0 10 10"><rect x="0.5" y="2" width="9" height="6" fill="var(--accent)"/><path d="M0.5 2 L5 5.5 L9.5 2" stroke="#fff" stroke-width="0.9" fill="none"/></svg>
          mail@copperlanepix.com.au
        </li>
        <li>
          <svg viewBox="0 0 10 10"><circle cx="5" cy="5" r="4.5" fill="var(--accent)"/><path d="M0.5 5 H9.5 M5 0.5 Q2.5 5 5 9.5 M5 0.5 Q7.5 5 5 9.5" stroke="#fff" stroke-width="0.7" fill="none"/></svg>
          www.copperlanepix.com.au
        </li>
      </ul>
    </div>
  </section>
  <section class="card card-back" role="img" aria-label="Card back: full-bleed brand artwork in warm orange tones"></section>
</main>
</body>
</html>
```